依頼詳細
タイトル+20~30行のテキストが主。
テキストをお読みいただき雰囲気に合ったデザインをお願いします。
イメージ
重厚感、誠実、まじめ。
もし動画にするならBGMはカゼノワの「白い石の坂道」のイメージ。
曇り空に一筋の光
とか
全面的に黒い雰囲気の中に一滴の赤

或いは画像の中の青空を活かしても面白いかもしれません。
記載項目
・添付のテキスト
・背景に使う写真は添付ファイルを使ってもいいし、使わなくても構いません
・最後の「松浦産業株式会社」は検索ウィンドウとし、右側に「検索」ボタンをつけてください。
・チラシ最下段に「説明会情報は弊社HPでご確認ください」
サイズ
A4
ページ数
片面
希望イメージ
シンプル 複雑
単色 カラフル
暗い 明るい
日常 高級
遊び心 厳粛
未来的 伝統的
女性的 男性的
希望する色
水色系、グレー系
納品ファイル
• フォトショップ形式 (.psd)
補足説明
追加でお願いするポスターは約72cm×22cmで一般的なサイズ
合同企業説明会のときにブースを通る学生さんの足を止めるためのインパクト大なポスターを希望します。

希望通りのイメージで仕上げて頂きました。
ありがとうございます。

多数のご提案頂きありがとうございました。

```html
<!DOCTYPE html>
<html lang="ja">
<head>
<meta charset="UTF-8">
<title>松浦産業株式会社 採用ポスター</title>
<link rel="stylesheet" href="https://fonts.googleapis.com/css2?family=Noto+Sans+JP:wght@400;500;700;900&display=swap">
<style>
  :root {
    --navy-deep: #0b1a2c;
    --navy: #1d3650;
    --sky: #5b8fbd;
    --sky-light: #cfe0ee;
    --haze: #eef3f7;
    --white: #ffffff;
    --ink: #111418;
    --brand: #1c3a5e;
    --rule: #9aa7b3;
  }
  * { margin: 0; padding: 0; box-sizing: border-box; }
  html, body { width: 849px; height: 1200px; overflow: hidden; background: var(--white); }
  .poster {
    position: relative;
    width: 849px;
    height: 1200px;
    overflow: hidden;
    font-family: "Noto Sans JP", sans-serif;
    background: var(--white);
  }
  .hero-photo {
    position: absolute;
    inset: 0 0 165px 0;
    background:
      radial-gradient(ellipse 260px 340px at 600px 220px, rgba(255,255,255,0.95), rgba(255,255,255,0) 70%),
      linear-gradient(100deg, var(--navy-deep) 0%, var(--navy) 38%, var(--sky) 60%, var(--sky-light) 78%, var(--haze) 100%);
  }
  .hero-photo::after {
    content: "";
    position: absolute;
    left: 0; right: 0; bottom: 0;
    height: 380px;
    background: linear-gradient(180deg, rgba(200,214,226,0) 0%, rgba(176,192,206,0.85) 60%, #c9d3dc 100%);
  }
  .manifesto {
    position: absolute;
    left: 40px;
    top: 28px;
    width: 480px;
    color: var(--white);
    font-size: 14px;
    font-weight: 500;
    line-height: 25px;
    letter-spacing: 0.04em;
  }
  .manifesto p { margin-bottom: 25px; }
  .manifesto p:last-child { margin-bottom: 0; }
  .headline {
    position: absolute;
    right: 62px;
    top: 28px;
    writing-mode: vertical-rl;
    font-size: 80px;
    font-weight: 900;
    line-height: 1.12;
    letter-spacing: 0.02em;
    color: var(--ink);
    background: rgba(255,255,255,0.55);
    padding: 10px 6px;
  }
  .footer {
    position: absolute;
    left: 0; right: 0; bottom: 0;
    height: 165px;
    background: var(--white);
    padding: 22px 0 0 40px;
    color: var(--brand);
  }
  .tagline { font-size: 27px; font-weight: 700; letter-spacing: 0.06em; }
  .company { font-size: 50px; font-weight: 900; letter-spacing: 0.04em; line-height: 1.25; margin-top: 4px; }
  .info-row { display: flex; align-items: center; gap: 14px; margin-top: 8px; }
  .info-note { font-size: 12px; color: var(--ink); }
  .search-button {
    border: 1px solid var(--rule);
    border-radius: 2px;
    font-size: 12px;
    padding: 1px 14px;
    color: var(--ink);
    background: #f4f6f8;
  }
</style>
</head>
<body>
  <div class="poster">
    <div class="hero-photo" role="img" aria-label="曇り空の光を背に立つ鉄柱と足場の手すりを握る作業用手袋の写真"></div>

    <div class="manifesto">
      <p>スーツを着た仕事が幸せだと思い込んでないか？</p>
      <p>人生にレールなんて無い。<br>あるのは自分と世界との関わりだけだ。<br>幸せを規定するのは世界じゃない。<br>自分自身だ。<br>全ての価値観を捨てたとき、<br>未来に何を掴むだろう。</p>
      <p>やりたいことが見つからないなんて当たり前だ。<br>試しに周りの大人に聞いてみたらいい。<br>「やりたいこと、仕事にできてますか？」<br>きっと曖昧な答えしか返ってこない。</p>
      <p>もう認めよう。<br>君は特別じゃない。<br>何者にもなれはしない。<br>埋没する個だ。<br>自分探しなんてもう十分だ。</p>
      <p>認めよう。<br>全てそこから始まる。</p>
      <p>誰もがみな目的地なんてわかってない。<br>それでも。<br>それでも少しずつ歩む。</p>
      <p>変わり続ける自分は会社に何を期待すればいいんだろう。</p>
    </div>

    <h1 class="headline">掴み取れ！<br>可能性はここにある。</h1>

    <footer class="footer">
      <p class="tagline">企業活動のその先を見据える</p>
      <p class="company">松浦産業株式会社</p>
      <div class="info-row">
        <span class="info-note">説明会情報は弊社HPでご確認ください。</span>
        <span class="search-button">検索</span>
      </div>
    </footer>
  </div>
</body>
</html>
```